LAW FIRM - RE-DESIGN - (professional, excellence, tradition and innovation)

We are a premier law firm in New South Wales, Australia. We pride ourselves on being cutting edge and up to date in our market.

Our firm formed in 1874 and has a particularly strong tradition within it's geographic footprint. acting for clients over multiple generations. Despite our regional background, our reputation for excellence has enable us to remain highly visible in a large area.

We have invested heavily in ensuring future planning of this business, and do so on a recurring basis. This has lead to a review of our existing web site.

Although serviceable we feel our previous website is out-of-date and not as in touch with the modern market. We are aware that for the emerging clients a web site is often the face of a firm and a failure to hold attention on the first page may fail to capture the client.

We are seeking designs to communicate the core values of professionalism and excellence. At the same time as maintaining traditional country values of honesty, integrity and hard work we strive to embrace changes to the law and technology.

Target Market(s)

Clients of Law Firm

Industry/Entity Type

Law Firm

Coding

Coded - Design and coding required

Number of Pages Required

5+ page

Requirements
Must have
• A strong sense of professionalism and excellence with a careful balance between traditional values and innovation.
Nice to have
• We have included within our design brief links to top competitors sites to assist for design concepts.

```html
<!DOCTYPE html>
<html lang="en">
<head>
<meta charset="utf-8">
<title>Carrow Law — Based in New England</title>
<link rel="stylesheet" href="https://fonts.googleapis.com/css2?family=Crimson+Text:ital,wght@0,400;0,600;0,700;1,400;1,600&family=Source+Sans+3:ital,wght@0,300;0,400;0,600;1,700&display=swap">
<style>
  :root {
    --white: #ffffff;
    --nav-grey: #d4d6d6;
    --panel-black: #000000;
    --accent-blue: #1d4a80;
    --button-top: #2a5a99;
    --button-bottom: #16427a;
    --footer-grey: #c5c2c5;
    --footer-text: #1b1b1b;
    --sky-top: #6f7a76;
    --sky-mid: #7d8782;
    --sea: #4a5a5c;
    --land: #5d6548;
    --bronze-light: #c58a52;
    --bronze-dark: #5a2f14;
  }
  * { box-sizing: border-box; margin: 0; padding: 0; }
  html, body { width: 1200px; height: 603px; overflow: hidden; }
  body { position: relative; background: var(--footer-grey); font-family: "Source Sans 3", sans-serif; }

  .hero {
    position: absolute; left: 0; top: 0; width: 1200px; height: 579px;
    background: linear-gradient(180deg, var(--sky-top) 0%, var(--sky-mid) 45%, var(--sea) 62%, var(--land) 100%);
  }
  .hero-statue {
    position: absolute; left: 0; top: 20px; width: 600px; height: 559px;
    background: radial-gradient(ellipse 45% 60% at 38% 55%, var(--bronze-light) 0%, #9a5e30 45%, rgba(90,47,20,0.6) 70%, rgba(90,47,20,0) 100%);
  }

  .brand {
    position: absolute; left: 144px; top: 14px;
    font-family: "Crimson Text", serif; font-weight: 600; font-size: 24px; line-height: 38px;
    color: var(--white);
  }

  .main-nav { position: absolute; right: 144px; top: 24px; display: flex; gap: 25px; }
  .main-nav a {
    font-family: "Source Sans 3", sans-serif; font-weight: 400; font-size: 11.5px;
    color: var(--nav-grey); text-decoration: none; letter-spacing: 0;
  }
  .main-nav a.is-current { color: var(--white); }

  .location {
    position: absolute; right: 144px; top: 222px; text-align: right; color: var(--white);
  }
  .location-kicker {
    display: block; font-family: "Source Sans 3", sans-serif; font-weight: 300;
    font-size: 30px; line-height: 34px; opacity: 0.9;
  }
  .location-name {
    display: block; font-family: "Crimson Text", serif; font-style: italic; font-weight: 600;
    font-size: 52px; line-height: 50px; opacity: 0.92;
  }

  .message-panel {
    position: absolute; left: 334px; top: 353px; width: 722px; height: 226px;
    background: var(--panel-black); border-top: 4px solid var(--accent-blue);
    padding: 26px 0 0 44px; color: var(--white);
  }
  .message-title {
    font-family: "Crimson Text", serif; font-weight: 600; font-size: 26px; line-height: 28px;
    letter-spacing: 0.2px;
  }
  .message-body {
    width: 640px; margin-top: 2px;
    font-size: 11.2px; line-height: 17.6px; font-weight: 400;
  }
  .message-actions { display: flex; gap: 8px; margin-top: 20px; }
  .practice-select {
    width: 180px; height: 34px; border: 1px solid var(--white);
    display: flex; align-items: center; justify-content: space-between; padding: 0 8px 0 12px;
    font-style: italic; font-weight: 700; font-size: 11.5px;
  }
  .contact-button {
    width: 134px; height: 34px; border-radius: 2px;
    background: linear-gradient(180deg, var(--button-top), var(--button-bottom));
    display: flex; align-items: center; justify-content: center;
    font-family: "Crimson Text", serif; font-weight: 700; font-size: 15px; color: var(--white);
    text-decoration: none;
  }

  .site-footer {
    position: absolute; left: 0; top: 579px; width: 1200px; height: 24px;
    background: var(--footer-grey);
  }
  .footer-line {
    position: absolute; right: 144px; top: 5px;
    font-family: "Crimson Text", serif; font-weight: 600; font-size: 10.5px; color: var(--footer-text);
  }
  .footer-line .label { color: var(--accent-blue); font-family: "Source Sans 3", sans-serif; font-weight: 700; }
  .footer-line .divider { margin: 0 5px; }
</style>
</head>
<body>
  <div class="hero" role="img" aria-label="Photo of a white lighthouse on a grassy coastal headland under an overcast sky"></div>
  <div class="hero-statue" role="img" aria-label="Bronze statue of Lady Justice holding scales"></div>

  <div class="brand">Carrow Law</div>

  <nav class="main-nav">
    <a class="is-current" href="#">HOME</a>
    <a href="#">ABOUT US</a>
    <a href="#">SERVICES</a>
    <a href="#">OUR PEOPLE</a>
    <a href="#">FAQS</a>
    <a href="#">CONTACT US</a>
  </nav>

  <div class="location">
    <span class="location-kicker">BASED IN</span>
    <span class="location-name">New England</span>
  </div>

  <section class="message-panel">
    <h1 class="message-title">YOUR MESSAGE GOES HERE</h1>
    <p class="message-body">Lorem ipsum dolor sit amet, consectetur adipiscing elit. Sed nec sem mattis, facilisis elit ut, maximus enim. Donec dui sem, fermentum a faucibus ac, tincidunt non ante. Aliquam condimentum dapibus orci, vitae mattis ante elementum nec. Sed vulputate vitae turpis ac hendrerit. Nunc pretium mollis elit, ut volutpat ipsum pretium ac. Nam dictum est vitae erat ultricies, posuere aliquam libero posuere. Mauris porttitor tincidunt nibh, et consequat nibh tincidunt sit amet. Quisque a orci felis. Ut ultrices fermentum risus sit amet eleifend. Quisque quis lobortis nulla. Vivamus vel justo id massa gravida vestibulum. Pellentesque porttitor convallis dui varius condimentum. Suspendisse potenti. Proin ullamcorper at nisl nec efficitur ultrices ex dignissimid.</p>
    <div class="message-actions">
      <div class="practice-select">
        <span>Select a Prcatical Area</span>
        <svg width="11" height="7" viewBox="0 0 11 7" aria-hidden="true"><path d="M1 1l4.5 4.5L10 1" fill="none" stroke="#ffffff" stroke-width="1.8"/></svg>
      </div>
      <a class="contact-button" href="#">CONTACT US »</a>
    </div>
  </section>

  <footer class="site-footer">
    <p class="footer-line"><span class="label">E:</span> info@carrowlaw.com.au<span class="divider">|</span>©2017 Carrow Law.</p>
  </footer>
</body>
</html>
```